Redesign of SnapHarbor Lumora Mobile app

The App exists, is up and running but the design is not the best (my creation and i am a developer).
Project landing page http://snapharbor.example/

Also the app has live tiles small, medium and large.

The purpose of this is to have a professional design and make this app the best app on the Lumora Mobile marketplace of his kind.

This app is a picture library that tells you where you've made you're pictures and gives you a unique perspective on the places that you have visited.

If this is successful there will be a version for Lumora 8, Zentrix and QOS also.

The app right now is for LM7 and LM8 and because of this the performance is not the best. With this new design the app will be for LM8 only and have the best performance possible.

I am not sure what else should i mention here but i am glad to answer to any questions if you are interested.

I am using Vantor draft as a design tool and Vantor Mixer and Crafton bench as development tools so if you can provide compatible file the better but is not mandatory.

It wold be nice to keep the existing color palette but again nothing is mandatory I just need a good design.

Links:
App on Marketplace http://www.appdepotmobile.example/en-us/store/app/snapharbor/7a3f9d21-0b6c-4e8d-9f12-ab34cd56ef78

App landing page http://snapharbor.example/
Updates

Reason: The submission time was extended doe to the request of designers.

We can do better, I will increase the budget with 200$  so the total budget will be 480$ so please consider this more seriously.

Thank you.

Target Market(s)

Lumora Mobile users that travel and make pictures.

Industry/Entity Type

Library

Requirements
Must have
• Panorama control as the App main page like in the present.

Representation of visited locations , Live tiles, Map, share location and picture..

If the designer comes up with better proposition they will be take in consideration.

None of these are mandatory but we should keep a connection with the present design so the users will not have the impression that this is a totally different app, this is SnapHarbor but better, more professional.

```html
<!DOCTYPE html>
<html lang="en">
<head>
<meta charset="utf-8">
<title>SnapHarbor – Locations</title>
<link rel="stylesheet" href="https://fonts.googleapis.com/css2?family=Open+Sans:wght@300;400&display=swap">
<style>
  :root {
    --page-bg: #ececec;
    --screen-bg: #9fb88a;
    --ink: #1b1b1b;
    --accent: #2a9fe0;
    --faded: rgba(40, 50, 40, 0.12);
    --caption-light: #ffffff;
    --card-border: #ffffff;
    --card-shadow: rgba(0, 0, 0, 0.35);
    --hills-top: #c9d6b4;
    --hills-mid: #9fc27e;
    --hills-low: #6f9a58;
    --tuscany-sky: #dfe6ee;
    --tuscany-town: #b59068;
    --tuscany-wall: #a0583c;
    --coast-sky: #3f8fd6;
    --coast-rock: #c7c3b8;
    --coast-card: #2c7fd0;
  }
  html, body {
    margin: 0;
    padding: 0;
    width: 1200px;
    height: 1000px;
    overflow: hidden;
    background: var(--page-bg);
    font-family: "Open Sans", "Segoe UI", sans-serif;
  }
  .app-screen {
    position: absolute;
    left: 252px;
    top: 214px;
    width: 768px;
    height: 786px;
    overflow: hidden;
    background: var(--screen-bg);
  }
  .panorama-background {
    position: absolute;
    inset: 0;
    background:
      linear-gradient(180deg,
        var(--hills-top) 0%,
        #b7ca9c 25%,
        var(--hills-mid) 55%,
        var(--hills-low) 80%,
        #5f7f4c 100%);
    opacity: 0.9;
  }
  .panorama-title {
    position: absolute;
    left: 24px;
    top: -8px;
    margin: 0;
    font-weight: 300;
    font-size: 168px;
    line-height: 1;
    letter-spacing: -2px;
    color: var(--ink);
    white-space: nowrap;
  }
  .pivot-headers {
    position: absolute;
    left: 38px;
    top: 206px;
    display: flex;
    gap: 36px;
    margin: 0;
    padding: 0;
    list-style: none;
    font-weight: 300;
    font-size: 62px;
    line-height: 1;
    white-space: nowrap;
  }
  .pivot-headers .pivot-item { color: var(--faded); }
  .pivot-headers .pivot-item.is-active { color: var(--accent); }

  .location-entry {
    position: absolute;
    left: 32px;
    width: 720px;
  }
  .location-entry.tuscany { top: 322px; }
  .location-entry.coast { top: 680px; }

  .photo-stack {
    position: absolute;
    left: 0;
    top: 0;
    width: 380px;
    height: 300px;
  }
  .photo-card {
    position: absolute;
    left: 8px;
    top: 8px;
    width: 350px;
    height: 266px;
    border: 6px solid var(--card-border);
    box-shadow: 0 2px 6px var(--card-shadow);
  }
  .photo-card.back-1 { transform: rotate(-3deg); }
  .photo-card.back-2 { transform: rotate(2.5deg); }
  .photo-card.front { transform: rotate(0.5deg); }

  .tuscany .photo-card.back-1,
  .tuscany .photo-card.back-2 { background: #8fa0b0; }
  .tuscany .photo-card.front {
    background: linear-gradient(180deg,
      var(--tuscany-sky) 0%, var(--tuscany-sky) 25%,
      var(--tuscany-town) 45%, #7e8a5a 62%,
      var(--tuscany-wall) 100%);
  }
  .coast .photo-card.back-1,
  .coast .photo-card.back-2 { background: var(--coast-card); }
  .coast .photo-card.front {
    background: linear-gradient(180deg,
      var(--coast-sky) 0%, #6aa8e0 25%,
      var(--coast-rock) 45%, #8e8a80 100%);
  }

  .location-summary {
    position: absolute;
    left: 392px;
    top: 150px;
    text-align: center;
    width: 320px;
  }
  .photo-count {
    margin: 0;
    font-weight: 300;
    font-size: 58px;
    line-height: 1.1;
    color: var(--ink);
  }
  .place-name {
    margin: 0;
    font-weight: 300;
    font-size: 42px;
    line-height: 1.2;
    color: var(--caption-light);
  }
</style>
</head>
<body>
  <main class="app-screen">
    <div class="panorama-background" role="img" aria-label="Soft-focus panorama of rolling green Tuscan hills with cypress trees"></div>

    <h1 class="panorama-title">SnapHarbor</h1>

    <ul class="pivot-headers">
      <li class="pivot-item">Recent</li>
      <li class="pivot-item is-active">Locations</li>
      <li class="pivot-item">Map</li>
    </ul>

    <section class="location-entry tuscany">
      <div class="photo-stack">
        <div class="photo-card back-1"></div>
        <div class="photo-card back-2"></div>
        <div class="photo-card front" role="img" aria-label="Photo of a yellow vintage car parked on a brick terrace overlooking a Tuscan hill town"></div>
      </div>
      <div class="location-summary">
        <p class="photo-count">24 Photos</p>
        <p class="place-name">Tuscany, Italy</p>
      </div>
    </section>

    <section class="location-entry coast">
      <div class="photo-stack">
        <div class="photo-card back-1"></div>
        <div class="photo-card back-2"></div>
        <div class="photo-card front" role="img" aria-label="Photo of pale rock formations under a bright blue sky"></div>
      </div>
    </section>
  </main>
</body>
</html>
```